PREMIUM AGENCY High End Business Card - A+++ Designers Wanted

** DO NOT ATTEMPT TO CONTACT ME THROUGH SEARCHING ON ZINTREL OR EMAILING ME THROUGH MY WEBSITE **

I need a fresh, contemporary business card designed using the logo attached (BRONSALK)

I have attached the font for BRONSALK

It must have a premium look and feel. The business card size must be STANDARD size.

You can submit either/both VERTICAL or HORIZONTAL designs.

FRONT: It must have the following sample information on

Paul Ardley
Director Operations
Mobile +61 452 118 906
Email paulardley@bronsalk.com
www.bronsalk.com

The REAR of the business card must have the words

CREATE INSPIRE TOMORROW

as part of the design, in the same font (NEXA) attached.

The words do not need to be in capitals, or on the same line, please design this as you see it best working.

ADDITIONAL INFORMATION
======================

The BRONSALK logo must be on the front of the card

I want Ultraviolet printing on the final design, to enhance either the NAME of the person OR the BRONSALK logo OR the words on the back of the card.

Target Market(s)

Agency, Advertising Agency, Creative, Designers

Industry/Entity Type

Media

Contact Information for Business Card

Design Agency, Contemporary, Premium look and feel, High Quality

Font styles to use
Serif
Sans Serif
Other font styles liked:
• ATTACHED TO PROJECT

Requirements
Must have
• BLACK & WHITE as the primary design, and if you feel there can be a highlighted colour, then this can be used.
• The Logo ICON attached is blue, this colour must not be changed.
• I have attached the partner brand BRONSALK MEDIA incase you need to manipulate the original files.
• ** DO NOT ATTEMPT TO CONTACT ME THROUGH SEARCHING ON ZINTREL OR EMAILING ME THROUGH MY WEBSITE **
Nice to have
• Must be Premium. I have attached some sample designs, that I like that would be a good inspiration for where this can be taken.
• My favourite design is is the KESTRAVUE2-BUSINESSCARD-TEMPLATE
Should not have
• No funny or silly standard / off the shelf designs

```html
<!DOCTYPE html>
<html lang="en">
<head>
<meta charset="utf-8">
<title>Bronsalk Media – Business Card</title>
<link rel="stylesheet" href="https://fonts.googleapis.com/css2?family=Mulish:wght@300;400;700;800&display=swap">
<style>
  :root {
    --page: #ffffff;
    --ink: #000000;
    --paper: #ffffff;
    --accent: #6eaae0;
  }
  * { margin: 0; padding: 0; box-sizing: border-box; }
  html, body {
    width: 1000px;
    height: 1200px;
    overflow: hidden;
    background: var(--page);
    font-family: "Mulish", "Helvetica Neue", Arial, sans-serif;
  }
  .sheet { position: relative; width: 1000px; height: 1200px; }

  .card { position: absolute; overflow: hidden; background: var(--accent); }
  .card--front { left: 222px; top: 142px; width: 553px; height: 359px; }
  .card--back  { left: 224px; top: 677px; width: 551px; height: 356px; }
  .card__shape { position: absolute; inset: 0; width: 100%; height: 100%; }

  .brand {
    position: absolute;
    left: 28px;
    top: 32px;
    display: flex;
    align-items: center;
    gap: 9px;
    font-size: 19px;
    font-weight: 700;
    letter-spacing: 1.6px;
    line-height: 1;
  }
  .brand__dot {
    width: 14px; height: 14px;
    border-radius: 50%;
    background: var(--accent);
  }
  .card--front .brand { color: var(--paper); }
  .card--back .brand { left: 27px; top: 33px; color: var(--ink); }
  .card--back .brand__dot { background: var(--paper); }

  .person__name {
    position: absolute;
    left: 24px;
    top: 66px;
    font-size: 86px;
    font-weight: 400;
    line-height: 1;
    color: var(--paper);
    letter-spacing: 0.5px;
    white-space: nowrap;
  }
  .person__role {
    position: absolute;
    left: 27px;
    top: 162px;
    font-size: 45px;
    font-weight: 300;
    line-height: 1;
    color: var(--paper);
    white-space: nowrap;
  }

  .contact {
    position: absolute;
    right: 27px;
    top: 253px;
    list-style: none;
    text-align: right;
    color: var(--ink);
    font-size: 21px;
    font-weight: 400;
    line-height: 26px;
  }
  .contact__item { display: flex; justify-content: flex-end; align-items: center; gap: 12px; }
  .contact__icon { width: 14px; height: 14px; flex: none; }

  .tagline {
    position: absolute;
    left: 27px;
    top: 162px;
    font-size: 30px;
    font-weight: 700;
    letter-spacing: 0.6px;
    line-height: 1;
    color: var(--paper);
    white-space: nowrap;
  }
</style>
</head>
<body>
<main class="sheet">

  <section class="card card--front" aria-label="Business card front">
    <svg class="card__shape" viewBox="0 0 553 359" preserveAspectRatio="none" aria-hidden="true">
      <path fill="var(--ink)" d="M0 0 H265 C275 15 280 40 285 55 C295 80 320 100 335 125 C355 160 355 195 340 225 C320 260 290 290 225 290 H200 C150 290 40 292 40 330 V359 H0 Z"/>
    </svg>
    <div class="brand"><span class="brand__dot"></span><span class="brand__name">BRONSALK MEDIA</span></div>
    <h1 class="person__name">Paul Ardley</h1>
    <p class="person__role">Director Operations</p>
    <ul class="contact">
      <li class="contact__item">
        <svg class="contact__icon" viewBox="0 0 14 14" aria-hidden="true"><rect x="3" y="1" width="8" height="12" rx="1" fill="none" stroke="var(--ink)" stroke-width="1.6"/><circle cx="7" cy="10.5" r="0.9" fill="var(--ink)"/></svg>
        <span>+61 452 118 906</span>
      </li>
      <li class="contact__item">
        <svg class="contact__icon" viewBox="0 0 14 14" aria-hidden="true"><circle cx="7" cy="7" r="5" fill="var(--ink)"/><path d="M4 6 Q6 4 8 6 T10 8" fill="none" stroke="var(--accent)" stroke-width="1"/></svg>
        <span>www.bronsalk.com</span>
      </li>
      <li class="contact__item">
        <svg class="contact__icon" viewBox="0 0 14 14" aria-hidden="true"><rect x="1" y="3" width="12" height="8" fill="none" stroke="var(--ink)" stroke-width="1.4"/><path d="M1 3 L7 8 L13 3" fill="none" stroke="var(--ink)" stroke-width="1.4"/></svg>
        <span>paulardley@bronsalk.com</span>
      </li>
    </ul>
  </section>

  <section class="card card--back" aria-label="Business card back">
    <svg class="card__shape" viewBox="0 0 551 356" preserveAspectRatio="none" aria-hidden="true">
      <path fill="var(--ink)" d="M288 0 H551 V356 H511 V335 C511 300 440 289 400 289 H330 C270 289 230 250 210 200 C195 165 205 140 225 115 C245 90 265 65 270 50 C275 30 280 12 288 0 Z"/>
    </svg>
    <div class="brand"><span class="brand__dot"></span><span class="brand__name">BRONSALK MEDIA</span></div>
    <p class="tagline">CREATE INSPIRE TOMORROW</p>
  </section>

</main>
</body>
</html>
```